Design a compelling Tarnwell Business Card that will drive people to my site

I want a business card that I can give to people—less to tell them who I am and more to direct them to my website. My website is a portal for Crestlane Aquatics Officials and a place for people who want to become Crestlane Aquatics Officials.
I am uploading my official company logo as well as a business card mockup that I did on my own. Please feel free to completely stray from this design.
I've included a screen recording of the homepage of my website as well.
Target Market(s)
Crestlane Aquatics Officials and people who desire to become one
Contact Information for Business Card
website url
Look and feel
Each slider illustrates characteristics of the customer's brand and the style your logo design should communicate.

```html
<!DOCTYPE html>
<html lang="en">
<head>
<meta charset="utf-8">
<title>Tarnwell Business Card</title>
<link href="https://fonts.googleapis.com/css2?family=Montserrat:wght@400;500;600;700&display=swap" rel="stylesheet">
<style>
  :root {
    --page-bg: #3a3a3a;
    --brand-blue: #3a56a8;
    --brand-light: #8da3d8;
    --ink: #2b3f8f;
    --text-dark: #3a3a46;
    --rule: #b9c6e6;
    --card-white: #ffffff;
  }
  * { box-sizing: border-box; margin: 0; padding: 0; }
  html, body { width: 1200px; height: 875px; overflow: hidden; }
  body {
    background: var(--page-bg);
    font-family: "Montserrat", Arial, sans-serif;
    display: flex;
    flex-direction: column;
    align-items: center;
    justify-content: center;
    gap: 48px;
  }
  .card {
    width: 640px;
    height: 366px;
    border-radius: 22px;
    position: relative;
    overflow: hidden;
    box-shadow: 0 10px 24px rgba(0,0,0,0.35);
  }
  .card-front {
    background: var(--brand-blue);
    display: flex;
    align-items: center;
    justify-content: center;
  }
  .brand-name {
    font-weight: 600;
    letter-spacing: -1px;
    line-height: 1;
  }
  .card-front .brand-name {
    color: var(--card-white);
    font-size: 104px;
  }
  .card-back { background: var(--card-white); }
  .card-back .brand-name {
    position: absolute;
    right: 52px;
    top: 58px;
    font-size: 60px;
    color: var(--ink);
  }
  .top-rule {
    position: absolute;
    left: 52px; right: 40px;
    top: 150px;
    height: 1px;
    background: var(--rule);
  }
  .contact-block {
    position: absolute;
    left: 52px;
    bottom: 36px;
    width: 260px;
  }
  .person-name {
    font-size: 26px;
    font-weight: 700;
    color: var(--ink);
  }
  .person-name .surname { color: var(--brand-light); }
  .person-title {
    font-size: 15px;
    color: var(--text-dark);
    margin-top: 2px;
  }
  .contact-rule {
    height: 1px;
    background: var(--rule);
    margin: 14px 0 12px;
  }
  .contact-list { list-style: none; }
  .contact-list li {
    display: flex;
    align-items: center;
    gap: 10px;
    font-size: 15px;
    color: var(--text-dark);
    line-height: 26px;
  }
  .contact-list svg { width: 14px; height: 14px; fill: var(--ink); flex: none; }
</style>
</head>
<body>
  <section class="card card-front">
    <span class="brand-name">tarnwell</span>
  </section>

  <section class="card card-back">
    <span class="brand-name">tarnwell</span>
    <div class="top-rule"></div>
    <div class="contact-block">
      <h1 class="person-name">Daniel <span class="surname">Marrow</span></h1>
      <p class="person-title">CEO &amp; Founder</p>
      <div class="contact-rule"></div>
      <ul class="contact-list">
        <li>
          <svg viewBox="0 0 24 24" aria-hidden="true"><path d="M6.6 10.8a15.1 15.1 0 0 0 6.6 6.6l2.2-2.2a1 1 0 0 1 1-.25 11.4 11.4 0 0 0 3.6.57 1 1 0 0 1 1 1V20a1 1 0 0 1-1 1A17 17 0 0 1 3 4a1 1 0 0 1 1-1h3.5a1 1 0 0 1 1 1c0 1.25.2 2.45.57 3.57a1 1 0 0 1-.25 1z"/></svg>
          (555) 214-7730
        </li>
        <li>
          <svg viewBox="0 0 24 24" aria-hidden="true"><path d="M2 5h20v14H2z M2 5l10 8 10-8" /></svg>
          dan@tarnwell.com
        </li>
        <li>
          <svg viewBox="0 0 24 24" aria-hidden="true"><circle cx="12" cy="12" r="10"/></svg>
          www.tarnwell.com
        </li>
      </ul>
    </div>
  </section>
</body>
</html>
```